Fun Project: Help Make A High Tech Company Look High Tech

Professional Website redesign for IT Maintenance Contract & Asset Management Services Company.

See their website below to understand who they are and what they do.

Note: This is for design only. No coding required. We want to see your ideas for a great website! This project will be a FUN design and not boring like others you may have worked on.

Please let your creative ideas flow. We have given you a ton of info along with videos to help you understand what we are after. However, we WANT your creativity to shine through in your designs!

You will be doing the homepage of this design. If you are chosen as the winner, we will ask for your help with an interior page design. However for the initial phases just the homepage is required.

We are a professional company that has run hundreds of crowdsourced projects on multiple platforms. If you participate in this contest (we hope you do) you can expect great video feedback and consistent feedback. We guarantee that if we know your website design will not be what we are looking for, we will notify you, so you don’t waste your time if there is no chance of you winning.

We respect and recognize this is how you make your living, and we will not play games. We look forward to an awesome contest and awesome website designs.

Design Brief:

We are looking for a fresh and professional new website design for Norvel Gear Stewards.

Here is their current website: http://norvelgearstewards.com/

This company is a high-tech company that serves their clients on many different levels. Please visit their site, read about them a bit so you can understand the products and services that they offer. This information will be very helpful in your design process.

They are in need of a fresh new website that needs to convey trust, professionalism, and high-tech while at the same time having some personality and standing out. We do not want to be boring or look like every other site in our industry.

Here is a video to help explain what we like about the current site and what we don’t like:

CURRENT SITE VIDEO: http://vidloopa.net/t/kPzRNe4Q

We want a website that is professional-looking. This website will be looked at by high-end decision makers in many sectors of business. We need the site to reflect very favorably on our company and to showcase our company in the best light.

Here are some examples of other sites in their business that have some things we like:

1. https://www.brimstead.com/ Please watch video to learn what we like and don’t like:

Brimstead Video: http://vidloopa.net/t/wMM4HjLo

Our client has said that if they could replace the name, and the proprietary info with their info on this site they would be very happy with the outcome. I know we can do better :)

2. http://valdroop.com/ Please watch video to learn what we like and don’t like:

Valdro Op Video: http://vidloopa.net/t/xUrPbdHzw

Our client has said that the like the sleekness of their homepage, but overall the site seems too simplistic and generic.

3. http://pallowringzz.com/ Please watch video to learn what we like and don’t like:

Pallow Ring Video: http://vidloopa.net/t/q3NoraW7Fdu

This site is a great example of a site that we would not want. Too simple, to old feeling, to outdated for the times and our industry.

NOTE: We do not want to copy anything outright. We want to learn, model and take their ideas and make them better. We also want you to be flexible and take what we like along with your creativity to make an amazing design.

We do not want templates, themes, or anything like that. We are looking for custom design. If we feel you are just using templates as a way to win, we will just disqualify you.

Here is what we are looking for in more specific terms:

Site structure: We want a horizontal header, horizontal menu, a place for video in the upper left-hand part of the site. We also want columns to help us separate the important parts of our business on the homepage into simple easy to identify parts.

Colors: We like the darker blue that conveys high tech, cyber, IT, servers, etc. You can see examples of the blues that we like in the brimstead video above.

Grays: Gray gives sites a high-tech feel if used right. I think you can see that in the Valdro video above.

Deep Purple: Our logo has a deep rich purple to it. This logo and it's colors helps us stand out in our industry. We will be keeping the logo and the colors so please work it into your design.

When looking at colors, please know that the current site and look is NOT what we are aiming for. We are going for a clean and professional look but also a look that is Bold and Vibrant (hence the colors).

Please use complementary colors on the site that blend well together to make an aesthetically pleasing design.

Menu: Horizontal. We like bold and easy to read menu items. Don’t make it small and cluttered.

Site Structure: Clean and easy to navigate. We have a lot of content to display, so we need a clean structure that breaks up the text and content areas.

Images: Please pull images from the current site or use stock footage.. We can always replace the images of course, but if you show them “their own industry” in the new design you will be closer to winning because it will feel more like “them”. We will purchase any images needed for the design once we choose a winner. We prefer Pixwell Bank and Imagora as images sources.

Look and Feel: Professional. Bold. High-End. Business-like. We have already stated many times the feel of this site.

Content Areas: It is a safe bet that if it is on the current site we need it on the new site. So don’t drop anything as it makes it hard to “cut content”. Feel free to arrange it however you see fit though.

What we don't want: We do not want clutter, boring, or templates or themes. We don’t want too cartoony, too cute, or too fancy. We do not want to look like other companies in our industry, and we do not want anything close to our current site. Be creative!

Out of respect to professional designers who are working hard to win if you do not follow this brief, you submit worn out themes, templates, or boring designs you will be eliminated from this contest. We are offering great prize money for this contest, so we expect great visual designs.

Here are some words that we would use that would help describe the type of site that we are looking for:

IT (information technology)
Cyber
Data
High Tech
Servers
Cloud Based
Automation
Silicon Valley
Global IT
Fiber Optic
Virtualization
Data Center
Enterprise Level Services
Storage (Big Data)
Network

We appreciate your interest in this contest. Please let us know if you have any question, need clarification, or any thoughts on this project to share with us. We are eager to work with you if you are interested in this contest.

Thanks!

Target Market(s)

The target market for our products and services is large corportations and divisions of goverment that need our services.

Industry/Entity Type

It Company

Number of Pages Required

1 page

Font styles to use
Sans Serif

Requirements
Must have
• Video integrated into design.
• Follow our brief
• Professional
• Bold
• Clean
Nice to have
• please follow our brief on this.
Should not have
• Clutter
• templates
• themes
• disorginazation

```html
<!DOCTYPE html>
<html lang="en">
<head>
<meta charset="utf-8">
<title>Norvel Gear Stewards</title>
<link href="https://fonts.googleapis.com/css2?family=Open+Sans:wght@400;600&family=Poiret+One&display=swap" rel="stylesheet">
<style>
:root{
  --purple:#2a0a6b;
  --purple-bar:#35117a;
  --ink:#3b3b3b;
  --light:#f0f0f2;
  --white:#fff;
  --navy:#1d2a5c;
  --sky:#e9eef5;
  --glass:#3f6aa6;
  --glass-deep:#14305e;
}
*{margin:0;padding:0;box-sizing:border-box}
html,body{width:1200px;height:2198px;overflow:hidden;background:var(--white)}
body{position:relative;font-family:"Open Sans",Arial,sans-serif;color:var(--ink)}
.abs{position:absolute}
.display{font-family:"Poiret One",sans-serif;font-weight:400;white-space:nowrap}

.top-rule{left:0;top:0;width:1200px;height:3px;background:var(--purple)}
.brand{left:98px;top:48px;display:flex;align-items:center;gap:12px}
.brand-dot{width:16px;height:16px;border-radius:50%;background:var(--purple)}
.brand-name{font-family:"Poiret One",sans-serif;font-size:25px;color:var(--purple)}
.utility{right:100px;top:50px;display:flex;align-items:center;font-size:12.5px;color:#333;gap:8px}
.utility .phone{font-size:16px;margin-right:22px;display:flex;align-items:center;gap:8px}
.utility .mail{display:flex;align-items:center;gap:8px;margin-right:22px}
.nav{right:100px;top:96px;display:flex;gap:34px;font-size:13px;color:#222}
.nav .active{position:relative}
.nav .active svg{position:absolute;left:-8px;top:20px}

.hero{left:0;top:157px;width:1200px;height:514px;
  background:
    radial-gradient(ellipse 380px 300px at 560px 40px,rgba(255,255,255,.95),rgba(255,255,255,0) 70%),
    linear-gradient(90deg,#2b4f86 0%,#5a80b6 10%,#9fb5d2 22%,rgba(214,224,236,0) 38%,rgba(214,224,236,0) 62%,#8aa4c8 74%,#3c63a0 86%,#1c3a70 100%),
    linear-gradient(180deg,var(--sky) 0%,#b9c9de 40%,var(--glass) 78%,var(--glass-deep) 100%)}
.hero-shade{left:0;top:621px;width:1200px;height:50px;background:linear-gradient(180deg,rgba(20,40,80,0),rgba(20,40,80,.35))}
.hero-title{left:367px;top:368px;font-size:28px;color:#1b1640}
.hero-sub{left:368px;top:410px;font-family:"Poiret One",sans-serif;font-size:15px;color:#1b1640}
.hero-arrow{top:390px}

.welcome{left:0;top:671px;width:1200px;height:344px;background:linear-gradient(180deg,#e4e4e8 0%,#fff 18%)}
.video{left:98px;top:722px;width:338px;height:240px;background:#fff;padding:4px;box-shadow:0 6px 12px rgba(0,0,0,.28)}
.video-still{width:100%;height:100%;position:relative;
  background:
    radial-gradient(ellipse 90px 120px at 110px 100px,rgba(230,235,245,.85),rgba(230,235,245,0) 70%),
    linear-gradient(90deg,#8ea6c4 0%,#c9d6e6 40%,#5d6f7a 62%,#27463a 78%,#4f8a62 90%,#1d2e26 100%)}
.video-still svg{position:absolute;left:144px;top:98px}
.welcome-title{left:497px;top:742px;font-size:28px;color:var(--purple)}
.welcome-text{left:465px;top:804px;width:552px;font-size:11.5px;line-height:20.5px;color:#444}
.btn{left:465px;top:926px;width:114px;height:36px;background:var(--purple);color:#fff;font-size:12.5px;display:flex;align-items:center;justify-content:center;border-radius:2px}

.services{left:0;top:1015px;width:1200px;height:535px;background:linear-gradient(180deg,#f3f3f5 0%,#e4e5ea 60%,#d8d9de 100%)}
.section-title{width:1200px;left:0;text-align:center;font-size:29px;color:var(--purple)}
.card{top:1124px;width:308px}
.card-img{height:197px}
.card-cap{height:53px;background:var(--purple);color:#fff;font-family:"Poiret One",sans-serif;font-weight:400;font-size:17px;display:flex;align-items:center;padding-left:15px;white-space:nowrap}
.card-text{padding:12px 18px 0;font-size:11px;line-height:17px;color:#444}
.ticks{list-style:none;margin-top:6px}
.ticks li{display:flex;align-items:center;gap:8px;height:25px}
.more{display:block;margin-top:6px;font-size:14px;color:var(--purple)}

.partners{left:0;top:1550px;width:1200px;height:225px;background:#fff}
.partner{top:1700px;font-size:24px;font-weight:600;color:var(--navy);width:180px;text-align:center}
.trademark{left:0;top:1775px;width:1200px;height:130px;background:var(--light)}
.badge{left:226px;top:1805px;width:72px;height:72px;border-radius:50%;background:#243a8c;border:4px solid #c9cde2}
.trademark-text{left:350px;top:1830px;font-size:19px;color:var(--purple)}

.footer{left:0;top:1905px;width:1200px;height:242px;background:var(--purple)}
.fcol{top:1932px;color:#fff}
.fhead{font-size:17px;font-weight:600;text-transform:uppercase;padding-bottom:7px;border-bottom:1px solid rgba(255,255,255,.55);display:inline-block}
.flinks{list-style:none;margin-top:16px;font-size:11px}
.flinks li{height:19.5px;display:flex;align-items:center;gap:4px}
.contact-row{display:flex;gap:16px;font-size:11.5px;line-height:18px;margin-top:16px}
.field{margin-top:14px;width:218px;height:29px;background:#fff;border-radius:3px;font-size:11px;color:#aaa;padding:7px 12px}
.subscribe{margin-top:15px;width:109px;height:37px;background:#3a3a3a;color:#fff;font-size:14px;font-weight:600;display:flex;align-items:center;justify-content:center;border-radius:2px}
.bottom{left:0;top:2147px;width:1200px;height:51px;background:var(--purple-bar)}
.copy{left:98px;top:2163px;font-size:11.5px;color:#fff}
.social{top:2158px;width:28px;height:28px;border-radius:50%;background:rgba(255,255,255,.25)}
</style>
</head>
<body>
<div class="abs top-rule"></div>

<header>
  <div class="abs brand"><span class="brand-dot"></span><span class="brand-name">Norvel Gear Stewards</span></div>
  <div class="abs utility">
    <span class="phone"><svg width="14" height="14" viewBox="0 0 24 24"><path fill="#222" d="M6.6 10.8a15 15 0 0 0 6.6 6.6l2.2-2.2c.3-.3.7-.4 1-.2 1.1.4 2.3.6 3.6.6.6 0 1 .4 1 1V20c0 .6-.4 1-1 1A17 17 0 0 1 3 4c0-.6.4-1 1-1h3.5c.6 0 1 .4 1 1 0 1.3.2 2.5.6 3.6.1.3 0 .7-.2 1z"/></svg>1-800-555-0147</span>
    <span class="mail"><svg width="16" height="12" viewBox="0 0 16 12"><rect width="16" height="12" rx="1" fill="var(--purple)"/><path d="M1 1l7 6 7-6" stroke="#fff" fill="none" stroke-width="1.3"/></svg>info@norvelgearstewards.com</span>
    <span>Login</span><span>|</span><span>Register</span><span>|</span><span>Support</span><span>|</span><span>Sitemap</span>
  </div>
  <nav class="abs nav">
    <span class="active">Home<svg width="52" height="10" viewBox="0 0 52 10"><path d="M1 8 Q26 -2 51 5" stroke="var(--purple)" stroke-width="2" fill="none"/></svg></span>
    <span>Services</span><span>Key Features</span><span>About Us</span><span>Our Cloud</span><span>Help Desk</span><span>My Portal</span><span>Contact Us</span>
  </nav>
</header>

<section>
  <div class="abs hero" role="img" aria-label="Upward view of glass office towers against a pale sky"></div>
  <div class="abs hero-shade"></div>
  <svg class="abs hero-arrow" style="left:38px" width="20" height="50" viewBox="0 0 20 50"><path d="M18 2 L2 25 L18 48" stroke="rgba(255,255,255,.7)" stroke-width="2" fill="none"/></svg>
  <svg class="abs hero-arrow" style="left:1140px" width="20" height="50" viewBox="0 0 20 50"><path d="M2 2 L18 25 L2 48" stroke="rgba(255,255,255,.8)" stroke-width="2" fill="none"/></svg>
  <h1 class="abs hero-title display">Best-of-breed Solution For IT Maintenance Contract</h1>
  <p class="abs hero-sub">Asset tracking by offering a comprehensive platform</p>
</section>

<section>
  <div class="abs welcome"></div>
  <div class="abs video">
    <div class="video-still" role="img" aria-label="Video still of two engineers at a laptop beside a server rack">
      <svg width="42" height="42" viewBox="0 0 42 42"><circle cx="21" cy="21" r="20" fill="rgba(255,255,255,.55)"/><path d="M16 12 L31 21 L16 30z" fill="#fff"/></svg>
    </div>
  </div>
  <h2 class="abs welcome-title display">Welcome To Norvel Gear Stewards</h2>
  <p class="abs welcome-text">NGS Offers a best-of-breed SaaS solution for consolidating, managing, tracking, and renewing your IT maintenance contracts as well as track your fixed assets. Regardless of your IT hardware brand, age, location, or SLA need, we build a custom solution fit for our client. Our innovative web-based portal and customer service team provides our clients with best-in-class IT service through a single comprehensive solution.</p>
  <a class="abs btn">Read More</a>
</section>

<section>
  <div class="abs services" role="img" aria-label="Faint grey backdrop of city towers and a crowd"></div>
  <h2 class="abs section-title display" style="top:1066px">Our Services</h2>

  <article class="abs card" style="left:99px">
    <div class="card-img" role="img" aria-label="Hand holding a glowing globe among digital interface panels" style="background:radial-gradient(circle 70px at 110px 80px,#7fd0ff,#2f86c8 55%,rgba(20,70,120,0) 100%),linear-gradient(135deg,#0b2447,#175a8c 55%,#0a1a33)"></div>
    <h3 class="card-cap">Maintance And Warranty Tracking</h3>
    <div class="card-text">
      <p>NGS is a powerful web-based tool to track the equipment and software support contracts and warranties deployed</p>
      <ul class="ticks"><li>✔ Contract Management Portal</li><li>✔ Flexibility</li></ul>
      <a class="more">Read more &gt;&gt;</a>
    </div>
  </article>

  <article class="abs card" style="left:446px">
    <div class="card-img" role="img" aria-label="Hand touching a glowing blue bar chart" style="background:radial-gradient(ellipse 120px 80px at 170px 90px,#6fa8ff,#2a5fd0 50%,rgba(10,30,90,0) 100%),linear-gradient(160deg,#061640,#123a9a 55%,#050f30)"></div>
    <h3 class="card-cap">Asset Management For The Enterprise</h3>
    <div class="card-text">
      <p>The NGS platform, as a leading asset management portal for external vendors or customers with manufacturer-specific plugins</p>
      <ul class="ticks"><li>✔ Asset Tracking</li><li>✔ Interface, Component Tracking</li></ul>
      <a class="more">Read more &gt;&gt;</a>
    </div>
  </article>

  <article class="abs card" style="left:792px">
    <div class="card-img" role="img" aria-label="Rows of server cabinets in a bright data center" style="background:linear-gradient(180deg,#dfe6ec 0%,#9fb4c0 18%,#3f7d92 40%,#2c5d70 62%,#c6d3da 80%,#eef2f4 100%)"></div>
    <h3 class="card-cap">Multi-platform IT Maintaince Solutions</h3>
    <div class="card-text">
      <p>NGS provides a single point of contact for purchasing, managing, consolidating, and renewing OEM IT hardware maintenance.</p>
      <ul class="ticks"><li>✔ Contract Management Portal</li><li>✔ Flexibility</li></ul>
      <a class="more">Read more &gt;&gt;</a>
    </div>
  </article>
</section>

<section>
  <div class="abs partners"></div>
  <h2 class="abs section-title display" style="top:1615px">Our Partners</h2>
  <svg class="abs" style="left:60px;top:1702px" width="12" height="22" viewBox="0 0 12 22"><path d="M10 2 L2 11 L10 20" stroke="#aaa" stroke-width="2" fill="none"/></svg>
  <svg class="abs" style="left:1134px;top:1702px" width="12" height="22" viewBox="0 0 12 22"><path d="M2 2 L10 11 L2 20" stroke="#aaa" stroke-width="2" fill="none"/></svg>
  <span class="abs partner" style="left:97px">Solvane</span>
  <span class="abs partner" style="left:301px">Kopryx</span>
  <span class="abs partner" style="left:508px">Harumeda</span>
  <span class="abs partner" style="left:713px">Trelloway</span>
  <span class="abs partner" style="left:918px">Netavion</span>
</section>

<section>
  <div class="abs trademark"></div>
  <div class="abs badge"></div>
  <p class="abs trademark-text display">Norvel Gear Stewards (NGS) logos are trademarks of Norvel Gear Stewards.</p>
</section>

<footer>
  <div class="abs footer"></div>
  <div class="abs fcol" style="left:98px">
    <h4 class="fhead" style="width:124px">Quick Links</h4>
    <ul class="flinks"><li>›&nbsp;Home</li><li>›&nbsp;Services</li><li>›&nbsp;Key Features</li><li>›&nbsp;About Us</li><li>›&nbsp;Our Cloud</li><li>›&nbsp;My Portal</li><li>›&nbsp;Contact Us</li></ul>
  </div>
  <div class="abs fcol" style="left:341px">
    <h4 class="fhead" style="width:124px">Sitemap</h4>
    <ul class="flinks"><li>›&nbsp;Veritus oportere</li><li>›&nbsp;Finibus Bonorum</li><li>›&nbsp;Dignissimos ducimus</li><li>›&nbsp;Blanditiis praesentium</li><li>›&nbsp;Mollitia animi</li></ul>
  </div>
  <div class="abs fcol" style="left:563px;width:230px">
    <h4 class="fhead" style="width:202px">Contact Details</h4>
    <div class="contact-row"><svg width="12" height="16" viewBox="0 0 12 16"><path d="M6 0a6 6 0 0 0-6 6c0 4.5 6 10 6 10s6-5.5 6-10a6 6 0 0 0-6-6zm0 8.5A2.5 2.5 0 1 1 6 3.5a2.5 2.5 0 0 1 0 5z" fill="#fff"/></svg><span>Lorem Ipsum is simply dummy text of the printing and type setting street-395001</span></div>
    <div class="contact-row" style="font-size:15px;align-items:center"><svg width="14" height="14" viewBox="0 0 24 24"><path fill="#fff" d="M6.6 10.8a15 15 0 0 0 6.6 6.6l2.2-2.2c.3-.3.7-.4 1-.2 1.1.4 2.3.6 3.6.6.6 0 1 .4 1 1V20c0 .6-.4 1-1 1A17 17 0 0 1 3 4c0-.6.4-1 1-1h3.5c.6 0 1 .4 1 1 0 1.3.2 2.5.6 3.6.1.3 0 .7-.2 1z"/></svg>+1 415 555 0183</div>
    <div class="contact-row" style="align-items:center"><svg width="16" height="11" viewBox="0 0 16 11"><rect x=".5" y=".5" width="15" height="10" fill="none" stroke="#fff"/><path d="M1 1l7 5 7-5" stroke="#fff" fill="none"/></svg>hello@norvelgearsteward.com</div>
  </div>
  <div class="abs fcol" style="left:884px;width:218px">
    <h4 class="fhead" style="width:202px">Newsletter Signup</h4>
    <p style="font-size:11px;line-height:18px;margin-top:14px">Lorem ipsum dolor sit amet, consectetur adipiscing elit,</p>
    <div class="field">Email address</div>
    <div class="subscribe">Subcribe</div>
  </div>
  <div class="abs bottom"></div>
  <p class="abs copy">Copyright 2015 &nbsp;Norvel Gear Steward. All Rights Reserved</p>
  <span class="abs social" style="left:996px"></span>
  <span class="abs social" style="left:1034px"></span>
  <span class="abs social" style="left:1072px"></span>
</footer>
</body>
</html>
```